Wandering Pine Fencing LLC. A Fencing Company.

Fencing Company. Specializing in all type of fencing. To include decks, piers, and fence repairs. Seeking to get a great design, as we are expecting to ship these out in a mass market. Contact Information is, Carl Vintson and Mitchell Dorrow. Phone number is 347-812-5593.

Industry/Entity Type

Fencing

Font styles to use
Serif

Requirements
Must have
• Free Estimates
Nice to have
• Pictures of fences and decks

```html
<!DOCTYPE html>
<html lang="en">
<head>
<meta charset="utf-8">
<title>Wandering Pine Fencing – Postcard</title>
<link rel="stylesheet" href="https://fonts.googleapis.com/css2?family=Libre+Baskerville:wght@400;700&display=swap">
<style>
  :root{
    --red:#b3171d;
    --charcoal:#2e2e30;
    --grey:#5b5b5e;
    --white:#ffffff;
    --ink:#2a2a2a;
    --stage:#d9d6d2;
  }
  *{box-sizing:border-box;margin:0;padding:0}
  html,body{width:900px;height:1200px;overflow:hidden}
  body{background:var(--stage);font-family:"Libre Baskerville",Georgia,serif;color:var(--ink);position:relative}
  .postcard{position:absolute;left:40px;width:820px;height:555px;background:var(--white);overflow:hidden;box-shadow:0 6px 18px rgba(0,0,0,.25)}
  .postcard--front{top:30px}
  .postcard--back{top:615px}
  .postcard svg.art{position:absolute;inset:0;width:820px;height:555px}
  .brand{position:absolute;display:flex;flex-direction:column;align-items:center;color:var(--ink)}
  .brand-mark{width:38px;height:38px;background:var(--charcoal);margin-bottom:8px}
  .brand-name{font-size:19px;line-height:1.2;text-align:center}
  .front-brand{left:30px;top:40px;width:260px}
  .headline{position:absolute;left:20px;top:246px;width:270px;color:var(--white);font-size:18px;line-height:1.4;text-transform:uppercase;text-align:center}
  .services{position:absolute;left:50px;top:322px;width:235px;font-size:14px;line-height:1.45;color:var(--ink);list-style:none}
  .services li{position:relative;padding-left:18px}
  .services li::before{content:"";position:absolute;left:0;top:7px;width:8px;height:8px;border-radius:50%;background:var(--red)}
  .services .estimate{font-weight:700;color:var(--red)}
  .contact-tag{position:absolute;left:40px;top:401px;color:var(--white);font-size:15px;text-transform:uppercase;letter-spacing:.5px}
  .owners{position:absolute;left:40px;top:470px;color:var(--white);font-size:12px;text-transform:uppercase;letter-spacing:.8px}
  .phone{display:flex;align-items:center;gap:8px;font-size:24px}
  .front-phone{position:absolute;left:40px;top:496px;color:var(--white)}
  .phone svg{width:20px;height:20px}
  .back-contact{position:absolute;left:70px;top:400px;color:var(--ink)}
  .back-contact .label{color:var(--red);font-size:16px;text-transform:uppercase;letter-spacing:.5px}
  .back-contact .names{font-size:10px;text-transform:uppercase;letter-spacing:.5px;margin-top:2px}
  .back-contact .phone{font-size:20px;margin-top:2px}
  .back-contact .phone svg{width:17px;height:17px}
  .back-brand{position:static;flex-direction:row;gap:8px;margin-top:8px}
  .back-brand .brand-mark{width:20px;height:20px;margin:0}
  .back-brand .brand-name{font-size:12px}
  .stamp{position:absolute;right:60px;top:60px;width:62px;height:72px;border:2px solid var(--grey)}
  .address-lines{position:absolute;right:40px;top:360px;width:270px}
  .address-lines span{display:block;height:1px;background:#9a9a9a;margin-bottom:26px}
</style>
</head>
<body>

<section class="postcard postcard--front">
  <svg class="art" viewBox="0 0 820 555">
    <defs>
      <linearGradient id="deckPhoto" x1="0" y1="0" x2="0" y2="1">
        <stop offset="0" stop-color="#7fb4e0"/>
        <stop offset=".35" stop-color="#6f9a45"/>
        <stop offset=".6" stop-color="#c9a57a"/>
        <stop offset="1" stop-color="#9c7249"/>
      </linearGradient>
      <linearGradient id="fenceCircle" x1="0" y1="0" x2="1" y2="1">
        <stop offset="0" stop-color="#8cb7d6"/>
        <stop offset=".5" stop-color="#6b8b45"/>
        <stop offset="1" stop-color="#8b4c2e"/>
      </linearGradient>
      <linearGradient id="deckCircle" x1="0" y1="0" x2="1" y2="1">
        <stop offset="0" stop-color="#5b7a3a"/>
        <stop offset="1" stop-color="#7a3f24"/>
      </linearGradient>
    </defs>
    <g role="img" aria-label="Photo of a wooden deck with railing, table and patio umbrella">
      <path d="M400 0 H820 V450 H380 C340 330 340 120 400 0 Z" fill="url(#deckPhoto)"/>
    </g>
    <path d="M0 230 H330 V310 H0 Z" fill="var(--red)"/>
    <path d="M0 393 H340 V428 H0 Z" fill="var(--red)"/>
    <rect x="0" y="450" width="820" height="105" fill="var(--charcoal)"/>
    <rect x="0" y="444" width="820" height="6" fill="var(--red)"/>
    <circle cx="390" cy="240" r="92" fill="var(--white)"/>
    <circle cx="390" cy="240" r="86" fill="var(--red)"/>
    <g role="img" aria-label="Photo of a wooden privacy fence in a garden">
      <circle cx="390" cy="240" r="78" fill="url(#fenceCircle)"/>
    </g>
    <circle cx="470" cy="378" r="64" fill="var(--white)"/>
    <circle cx="470" cy="378" r="58" fill="var(--red)"/>
    <g role="img" aria-label="Photo of a stained wooden deck">
      <circle cx="470" cy="378" r="51" fill="url(#deckCircle)"/>
    </g>
  </svg>

  <div class="brand front-brand">
    <span class="brand-mark"></span>
    <span class="brand-name">Wandering Pine<br>Fencing</span>
  </div>
  <h1 class="headline">Specializing in all<br>type of fencing</h1>
  <ul class="services">
    <li>To include decks, piers, and fence repairs</li>
    <li class="estimate">Free Estimates</li>
  </ul>
  <p class="contact-tag">Contact Information</p>
  <p class="owners">Carl Vintson and Mitchell Dorrow</p>
  <p class="phone front-phone">
    <svg viewBox="0 0 24 24"><path fill="#e03a3e" d="M6.6 10.8a15 15 0 0 0 6.6 6.6l2.2-2.2c.3-.3.7-.4 1-.2 1.1.4 2.3.6 3.6.6.6 0 1 .4 1 1V20c0 .6-.4 1-1 1A17 17 0 0 1 3 4c0-.6.4-1 1-1h3.5c.6 0 1 .4 1 1 0 1.3.2 2.5.6 3.6.1.3 0 .7-.2 1z"/></svg>
    347-812-5593
  </p>
</section>

<section class="postcard postcard--back">
  <svg class="art" viewBox="0 0 820 555">
    <defs>
      <linearGradient id="housePhoto" x1="0" y1="0" x2="1" y2="1">
        <stop offset="0" stop-color="#d98a2b"/>
        <stop offset=".45" stop-color="#e8d9a8"/>
        <stop offset=".75" stop-color="#e9e9e4"/>
        <stop offset="1" stop-color="#5c7a3a"/>
      </linearGradient>
      <linearGradient id="railCircle" x1="0" y1="0" x2="1" y2="1">
        <stop offset="0" stop-color="#9ab868"/>
        <stop offset="1" stop-color="#8a4a2a"/>
      </linearGradient>
      <linearGradient id="fadedFence" x1="0" y1="0" x2="0" y2="1">
        <stop offset="0" stop-color="#e4e4e4"/>
        <stop offset="1" stop-color="#f7f7f7"/>
      </linearGradient>
    </defs>
    <g role="img" aria-label="Photo of a white picket fence before a house in autumn">
      <path d="M0 0 H480 C460 120 420 200 370 260 H0 Z" fill="url(#housePhoto)"/>
    </g>
    <g role="img" aria-label="Faded photo of a white fence along a lawn">
      <path d="M0 260 H370 C340 300 330 340 330 385 H0 Z" fill="url(#fadedFence)"/>
    </g>
    <path d="M480 0 C460 120 420 200 370 260 C320 330 330 450 400 555" fill="none" stroke="var(--red)" stroke-width="6"/>
    <path d="M500 0 C480 125 442 208 392 268 C345 335 355 450 424 555" fill="none" stroke="#c9c9c9" stroke-width="2"/>
    <circle cx="445" cy="115" r="92" fill="var(--white)"/>
    <circle cx="445" cy="115" r="86" fill="var(--red)"/>
    <g role="img" aria-label="Photo of a wooden deck railing">
      <circle cx="445" cy="115" r="78" fill="url(#railCircle)"/>
    </g>
    <rect x="0" y="505" width="55" height="50" fill="var(--red)"/>
  </svg>

  <div class="stamp"></div>
  <div class="address-lines"><span></span><span></span><span></span></div>

  <div class="back-contact">
    <p class="label">Contact</p>
    <p class="names">Carl Vintson and Mitchell Dorrow</p>
    <p class="phone">
      <svg viewBox="0 0 24 24"><path fill="#b3171d" d="M6.6 10.8a15 15 0 0 0 6.6 6.6l2.2-2.2c.3-.3.7-.4 1-.2 1.1.4 2.3.6 3.6.6.6 0 1 .4 1 1V20c0 .6-.4 1-1 1A17 17 0 0 1 3 4c0-.6.4-1 1-1h3.5c.6 0 1 .4 1 1 0 1.3.2 2.5.6 3.6.1.3 0 .7-.2 1z"/></svg>
      347-812-5593
    </p>
    <div class="brand back-brand">
      <span class="brand-mark"></span>
      <span class="brand-name">Wandering Pine Fencing</span>
    </div>
  </div>
</section>

</body>
</html>
```